Concrete Grinding and Polishing company business card with logo, based in Australia.

We need a business card design along with logo for a new company based in Melbourne called BrightLap. We specialise in the grinding and polishing of concrete. Polished concrete is durable, easy to maintain, cost effective, dust proof, has increased light reflectivity, and is slip resistant, among other benefits. In short, polished concrete is a popular flooring solution because of its practical advantages, as well as it's decorative appeal.

Industry/Entity Type

Business

Requirements
Must have
• It must have the company name(BrightLap) as well as the slogan: A Cut Above The Rest.
Nice to have
• Something that symbolises polished concrete. Would also like it to have a silver background with black writing, if possible.

```html
<!DOCTYPE html>
<html lang="en">
<head>
<meta charset="utf-8">
<title>BrightLap Business Card</title>
<link rel="stylesheet" href="https://fonts.googleapis.com/css2?family=Oswald:wght@300;500&family=Jura:wght@600&display=swap">
<style>
  :root {
    --backdrop: #000000;
    --card-top: #ffffff;
    --card-mid: #e6e6e6;
    --card-bottom: #bdbdbd;
    --ink: #111111;
    --slogan: #f4f4f4;
    --slogan-shadow: rgba(0, 0, 0, 0.55);
  }
  html, body {
    margin: 0;
    padding: 0;
    width: 1200px;
    height: 900px;
    overflow: hidden;
    background: var(--backdrop);
  }
  .canvas {
    position: relative;
    width: 1200px;
    height: 900px;
    background: var(--backdrop);
  }
  .card {
    position: absolute;
    left: 44px;
    top: 112px;
    width: 1106px;
    height: 678px;
    border-radius: 30px;
    background: linear-gradient(180deg, var(--card-top) 0%, var(--card-mid) 45%, var(--card-bottom) 100%);
  }
  .brand-name {
    position: absolute;
    left: 86px;
    top: 72px;
    margin: 0;
    font-family: "Oswald", sans-serif;
    font-weight: 500;
    font-size: 74px;
    line-height: 1;
    letter-spacing: 0.09em;
    color: var(--ink);
  }
  .slogan {
    position: absolute;
    left: 300px;
    top: 244px;
    margin: 0;
    font-family: "Oswald", sans-serif;
    font-weight: 300;
    font-size: 52px;
    line-height: 1;
    letter-spacing: 0.3em;
    color: var(--slogan);
    text-shadow: 4px 5px 6px var(--slogan-shadow);
    white-space: nowrap;
  }
  .contact {
    position: absolute;
    left: 86px;
    top: 474px;
    margin: 0;
    font-style: normal;
    font-family: "Jura", sans-serif;
    font-weight: 600;
    font-size: 33px;
    line-height: 48px;
    letter-spacing: 0.41em;
    color: var(--ink);
    white-space: nowrap;
  }
  .contact span { display: block; }
</style>
</head>
<body>
  <main class="canvas">
    <section class="card">
      <h1 class="brand-name">BrightLap</h1>
      <p class="slogan">A Cut Above The Rest</p>
      <address class="contact">
        <span class="contact-address">YOUR OFFICE ADDRESS</span>
        <span class="contact-web">WWW.YOURSITE.COM</span>
        <span class="contact-phone">(03)555-0142</span>
      </address>
    </section>
  </main>
</body>
</html>
```